Audio Tour Poster

I need a poster to show information on a audio tour ... walk ... bike etc ... the poster needs to be generic so that it could be used for several projects ... a space needs to be left to add a tour title and another area where a tri fold brochure can be placed for people to access ... the tri fold poster will be based on 8.5 x 14 inch legal size ...

The size of the final poster will be 18x 24 inches ... an example of a audio tour can be found at
http://trallexo.com/walk/568 or http://trallexo.com/walk/2507

Industry/Entity Type

Legal

```html
<!DOCTYPE html>
<html lang="en">
<head>
<meta charset="utf-8">
<title>Trallexo Audio Tour Poster</title>
<link href="https://fonts.googleapis.com/css2?family=Montserrat:wght@700;800&family=Arimo:wght@400&display=swap" rel="stylesheet">
<style>
:root{
  --plum:#a0166f;
  --plum-bright:#cd3a98;
  --plum-soft:#f3d9e9;
  --plum-mist:#e7b6d4;
  --paper:#ffffff;
  --stage:#ececec;
  --grey-box:#d6d6d6;
  --photo:#888888;
  --ink:#9b1469;
}
*{margin:0;padding:0;box-sizing:border-box}
html,body{width:900px;height:1200px;overflow:hidden}
body{background:var(--stage);position:relative;font-family:"Arimo",Arial,sans-serif}
.poster{
  position:absolute;left:30px;top:40px;width:682px;height:910px;
  transform:scale(1.2317);transform-origin:0 0;
  background:var(--paper);overflow:hidden;
}
.header{position:absolute;left:0;top:0;width:682px;height:110px;background:var(--plum)}
.brand{
  position:absolute;left:52px;top:30px;display:flex;align-items:center;gap:10px;
  color:var(--paper);font-family:"Montserrat",sans-serif;font-weight:800;font-size:36px;letter-spacing:1px;
}
.brand-dot{width:22px;height:22px;border-radius:50%;background:var(--paper)}
.tour-title{
  position:absolute;left:280px;top:30px;color:var(--paper);
  font-family:"Montserrat",sans-serif;font-weight:800;font-size:32px;letter-spacing:1.5px;line-height:1;
}
.headline{
  position:absolute;left:282px;top:68px;color:var(--paper);
  font-family:"Montserrat",sans-serif;font-weight:700;font-size:17.5px;letter-spacing:.6px;
}
.stripe{position:absolute;left:0;width:682px;height:15px;
  background:linear-gradient(90deg,var(--plum-bright),var(--plum-soft) 20%,var(--paper) 50%,var(--plum-soft) 80%,var(--plum-bright))}
.stripe.top{top:110px}
.stripe.bottom{top:437px;height:16px}
.gallery-band{position:absolute;left:0;top:125px;width:682px;height:312px;
  background:radial-gradient(ellipse at 50% 55%,var(--plum-bright) 0%,#b92585 45%,var(--plum) 80%)}
.polaroid{position:absolute;background:var(--paper);padding:10px 10px 0;box-shadow:2px 4px 8px rgba(0,0,0,.35)}
.polaroid .photo{background:var(--photo);width:100%}
.polaroid.left{left:28px;top:170px;width:232px;height:248px;transform:rotate(-5deg)}
.polaroid.left .photo{height:172px}
.polaroid.center{left:205px;top:128px;width:260px;height:292px;padding:0}
.polaroid.center .photo{height:216px}
.polaroid.right{left:425px;top:165px;width:226px;height:232px;transform:rotate(5deg)}
.polaroid.right .photo{height:165px}
.copy{color:var(--ink);font-size:11.4px;line-height:15.6px}
.copy-box{position:absolute;background:var(--grey-box)}
.copy-box.first{left:60px;top:455px;width:530px;height:130px;padding:14px 26px 0 20px}
.copy-box.second{left:58px;top:598px;width:575px;height:140px;padding:14px 46px 0 22px;transform:rotate(-2deg)}
.copy-column{position:absolute;left:82px;top:757px;width:128px;font-size:8px;line-height:11.7px}
.snapshot{position:absolute;background:var(--paper);padding:5px;box-shadow:2px 3px 7px rgba(0,0,0,.35)}
.snapshot .photo{background:var(--photo);width:100%;height:100%}
.snapshot.back{left:345px;top:675px;width:258px;height:140px;transform:rotate(-4deg)}
.snapshot.front{left:225px;top:728px;width:218px;height:126px;transform:rotate(3deg)}
.footer-wedge{position:absolute;left:0;top:0}
.art{position:absolute}
.art.beach{left:0;top:500px;width:52px;height:120px;background:linear-gradient(160deg,var(--plum-soft),var(--plum-mist));border-radius:0 8px 8px 0}
.art.travellers{left:458px;top:828px;width:140px;height:58px;background:linear-gradient(160deg,var(--plum-mist),var(--plum-bright));border-radius:8px}
.art.camera{left:620px;top:732px;width:48px;height:42px;background:var(--plum);border-radius:8px}
</style>
</head>
<body>
<main class="poster">
  <header class="header">
    <div class="brand"><span>Trallexo</span><span class="brand-dot"></span></div>
    <h1 class="tour-title">TITLE TOUR HERE</h1>
    <p class="headline">Put headline text here put the</p>
  </header>
  <div class="stripe top"></div>
  <section class="gallery-band"></section>
  <div class="polaroid left"><div class="photo" role="img" aria-label="Tour photo"></div></div>
  <div class="polaroid center"><div class="photo" role="img" aria-label="Main tour photo"></div></div>
  <div class="polaroid right"><div class="photo" role="img" aria-label="Tour photo"></div></div>
  <div class="stripe bottom"></div>

  <div class="art beach" role="img" aria-label="Illustration of a person relaxing under a beach umbrella"></div>

  <div class="copy-box first copy">Lorem ipsum dolor sit amet, consectetuer adipiscing elit, sed diam nonummy nibh euismod tincidunt ut laoreet dolore magna aliquam erat volutpat. Ut wisi enim ad minim veniam, quis nostrud exerci tation ullamcorper suscipit lobortis nisl ut aliquip ex ea commodo consequat. Duis autem vel eum iriure dolor in hendrerit in vulputate velit esse molestie consequat, vel illum dolore eu feugiat nulla facilisis at vero eros et accumsan et iusto odio dignissim qui blandit praesent luptatum zzril delenit augue duis dolore te feugait nulla facilisi. Nam liber tempor cum soluta nobis eleifend</div>

  <div class="copy-box second copy">Lorem ipsum dolor sit amet, consectetuer adipiscing elit, sed diam nonummy nibh euismod tincidunt ut laoreet dolore magna aliquam erat volutpat. Ut wisi enim ad minim veniam, quis nostrud exerci tation ullamcorper suscipit lobortis nisl ut aliquip ex ea commodo consequat. Duis autem vel eum iriure dolor in hendrerit in vulputate velit esse molestie consequat, vel illum dolore eu feugiat nulla</div>

  <p class="copy copy-column">Lorem ipsum dolor sit amet, consectetuer adipiscing elit, sed diam nonummy nibh euismod tincidunt ut laoreet dolore magna aliquam erat volutpat. Ut wisi enim ad minim veniam, quis nostrud exerci tation ullamcorper suscipit lobortis nisl ut aliquip ex ea commodo consequat. Duis autem vel eum</p>

  <svg class="footer-wedge" width="682" height="910" viewBox="0 0 682 910" aria-hidden="true">
    <polygon points="455,910 682,842 682,910" fill="var(--plum)"/>
  </svg>

  <div class="snapshot back"><div class="photo" role="img" aria-label="Tour snapshot"></div></div>
  <div class="snapshot front"><div class="photo" role="img" aria-label="Tour snapshot"></div></div>

  <div class="art travellers" role="img" aria-label="Illustration of a walker and a cyclist"></div>
  <div class="art camera" role="img" aria-label="Camera illustration"></div>
</main>
</body>
</html>
```